Vintage label design for Electrical company (stickers)

I'm after a vintage label design for my electrical company, currently trying to break into the upper market in the electrical field so I need something that stands out and is easy to read.
These will be getting made into stickers roughly 90-110mm x 40-60mm with a custom rectangular shape.
The stickers should have

Target Market(s)

Upper electrical market

Industry/Entity Type

Electrical

Font styles to use
Serif
Decorative
Script

Colors
acd037
9ccb3b
33b8a4

Requirements
Must have
• Be unique, edgy, vintage/retro and easy to read. An electrical theme
• Company logo (picture provided below obviously a lime)
• Fern Voltworks
• 0428915043
• Fernvoltworks.com
• plain circle symbol
• as these are going to be stickers I would like my contact details on them
Nice to have
• Same shades of green, fit between 90-110mm x 40-60mm

```html
<!DOCTYPE html>
<html lang="en">
<head>
<meta charset="utf-8">
<title>Fern Voltworks Sticker Label</title>
<link rel="stylesheet" href="https://fonts.googleapis.com/css2?family=Cinzel:wght@400;600&family=Montserrat:wght@500;600;700&display=swap">
<style>
  :root {
    --bg: #ececec;
    --forest: #1f5a25;
    --forest-deep: #184a1d;
    --leaf: #8fd06b;
    --leaf-soft: #9ccb3b;
    --lime-text: #7cc466;
    --paper: #ffffff;
    --banner-text: #e4eedc;
    --dash: rgba(255,255,255,0.75);
  }
  * { margin: 0; padding: 0; box-sizing: border-box; }
  html, body { width: 1200px; height: 836px; overflow: hidden; background: var(--bg); }
  .sticker {
    position: absolute; left: 190px; top: 118px;
    width: 820px; height: 600px;
    background: linear-gradient(135deg, var(--forest), var(--forest-deep));
  }
  .sticker__cutline {
    position: absolute; inset: 12px;
    border: 1px dashed var(--dash);
  }
  .sticker__frame { position: absolute; inset: 0; }
  .banner {
    position: absolute; left: 245px; top: 92px;
    width: 330px; height: 50px; border-radius: 12px;
    background: var(--forest);
    display: flex; align-items: center; justify-content: center;
    font-family: "Cinzel", serif; font-weight: 400; font-size: 30px;
    letter-spacing: 1px; color: var(--banner-text);
  }
  .brand {
    position: absolute; left: 0; right: 0; top: 165px;
    display: flex; flex-direction: column; align-items: center; gap: 14px;
  }
  .brand__dot {
    width: 74px; height: 74px; border-radius: 50%;
    background: var(--leaf);
  }
  .brand__name {
    font-family: "Cinzel", serif; font-weight: 600; font-size: 42px;
    color: var(--forest);
  }
  .contact {
    position: absolute; left: 0; right: 0; top: 375px;
    display: flex; flex-direction: column; align-items: center;
    font-family: "Montserrat", sans-serif;
  }
  .contact__social {
    width: 28px; height: 28px; border-radius: 50%;
    background: var(--forest); margin-bottom: 10px;
  }
  .contact__phone {
    font-weight: 600; font-size: 30px; letter-spacing: 2px;
    color: var(--lime-text); line-height: 1.05;
  }
  .contact__web {
    font-weight: 700; font-size: 14px; letter-spacing: 1px;
    color: var(--forest); margin-top: 4px;
  }
  .contact__licence {
    font-weight: 600; font-size: 11px; letter-spacing: 1px;
    color: var(--lime-text); margin-top: 6px;
  }
</style>
</head>
<body>
  <div class="sticker">
    <div class="sticker__cutline"></div>
    <svg class="sticker__frame" width="820" height="600" viewBox="0 0 820 600">
      <defs>
        <path id="plaque" d="M70 150 L110 150 Q120 110 160 105 L190 105 Q200 60 250 55 L570 55 Q620 60 630 105 L660 105 Q700 110 710 150 L750 150 L750 430 Q700 435 700 480 L700 500 Q660 505 650 545 L170 545 Q160 505 120 500 L120 480 Q120 435 70 430 Z"/>
      </defs>
      <use href="#plaque" fill="var(--leaf)"/>
      <use href="#plaque" fill="var(--forest)" transform="translate(410 300) scale(0.965 0.955) translate(-410 -300)"/>
      <use href="#plaque" fill="var(--leaf)" transform="translate(410 300) scale(0.955 0.942) translate(-410 -300)"/>
      <use href="#plaque" fill="var(--paper)" transform="translate(410 300) scale(0.94 0.922) translate(-410 -300)"/>
    </svg>
    <div class="banner">FERN VOLTWORKS</div>
    <div class="brand">
      <div class="brand__dot"></div>
      <div class="brand__name">Fern Voltworks</div>
    </div>
    <div class="contact">
      <div class="contact__social"></div>
      <div class="contact__phone">0428915043</div>
      <div class="contact__web">FERNVOLTWORKS.COM</div>
      <div class="contact__licence">R.E.C 40872</div>
    </div>
  </div>
</body>
</html>
```